Full service residential and commercial painting
Finest quality attention to detail
All workmanship guaranteed
Email :brunomdufay@postvale.fr
Mobile: 0417386250
Industry/Entity Type
Residential
Contact Information for Business Card
Marten Dufay painting & decorating
Requirements
Nice to have
- Am thinking about someone can be painting my name on the card with MD painting with the logos of brush,pot tray and roller sleeves

```html
<!DOCTYPE html>
<html lang="en">
<head>
<meta charset="utf-8">
<title>MD Painting – Business Card</title>
<link rel="stylesheet" href="https://fonts.googleapis.com/css2?family=Arimo:wght@400;700&display=swap">
<style>
  :root {
    --backdrop: #4a4a4a;
    --card: #fbfbfa;
    --ochre-light: #e2b43e;
    --ochre: #d3a12a;
    --ochre-deep: #b9891c;
    --orange: #f0960f;
    --grey-text: #6b6b6b;
    --ink: #222222;
  }
  * { margin: 0; padding: 0; box-sizing: border-box; }
  html, body {
    width: 1200px;
    height: 900px;
    overflow: hidden;
  }
  body {
    background: var(--backdrop);
    font-family: "Arimo", Arial, sans-serif;
    position: relative;
  }
  .business-card {
    position: absolute;
    left: 150px;
    top: 185px;
    width: 900px;
    height: 530px;
    background: var(--card);
    border-radius: 22px;
    overflow: hidden;
    box-shadow: 0 18px 40px rgba(0,0,0,0.35);
  }
  .painted-wall {
    position: absolute;
    left: 0;
    top: 0;
    width: 420px;
    height: 100%;
  }
  .brand {
    position: absolute;
    left: 470px;
    top: 42px;
  }
  .brand-name {
    font-weight: 700;
    font-size: 60px;
    line-height: 1;
    color: var(--orange);
    letter-spacing: 0.5px;
  }
  .brand-tagline {
    margin-top: 8px;
    font-size: 17px;
    color: var(--grey-text);
  }
  .services {
    position: absolute;
    right: 100px;
    top: 222px;
    text-align: right;
    list-style: none;
    font-size: 19px;
    line-height: 24px;
    color: var(--grey-text);
  }
  .contact {
    position: absolute;
    right: 100px;
    top: 372px;
    text-align: right;
  }
  .contact-name {
    font-size: 30px;
    color: var(--orange);
    margin-bottom: 10px;
  }
  .contact-line {
    font-size: 18px;
    line-height: 24px;
    color: var(--ink);
  }
</style>
</head>
<body>
  <article class="business-card">
    <svg class="painted-wall" viewBox="0 0 420 530" role="img" aria-label="Photo of a hand rolling ochre paint onto a white wall with a paint roller" preserveAspectRatio="none">
      <defs>
        <linearGradient id="wallPaint" x1="0" y1="0" x2="1" y2="1">
          <stop offset="0" stop-color="var(--ochre-light)"/>
          <stop offset="0.6" stop-color="var(--ochre)"/>
          <stop offset="1" stop-color="var(--ochre-deep)"/>
        </linearGradient>
      </defs>
      <path d="M0 0 H330 L340 60 L355 120 L340 200 L320 250 L290 320 L230 390 L180 450 L150 530 H0 Z" fill="url(#wallPaint)"/>
    </svg>

    <header class="brand">
      <h1 class="brand-name">MD Painting</h1>
      <p class="brand-tagline">Marten Dufay painting &amp; decorating</p>
    </header>

    <ul class="services">
      <li>Full service residential and commercial painting</li>
      <li>Finest quality attention to detail</li>
      <li>All workmanship guaranteed</li>
    </ul>

    <address class="contact" style="font-style: normal;">
      <p class="contact-name">Marten Dufay</p>
      <p class="contact-line">brunomdufay@postvale.fr</p>
      <p class="contact-line">Mobile : 0417386250</p>
    </address>
  </article>
</body>
</html>
```